carobrookcare needs a 4.6 handout

i need a styalized 4x6 postcard sized handout to leave on cars at shopping plazas and apartment buildings. WE are a medical marijuana referal clinic in brockton MA and we write perscriptions for qualifying patients, i have attached a pdf file of the content i need included in the hand out but please do not limit yourself if you feel like you could word it better. it is important to have our contact info front and center
Target Market(s)
potential medical marijuana patients
Industry/Entity Type
Apartment
Requirements
Must have
- the content listed inside the PDF file i attached
Nice to have
- must have everything in the PDF file. should be colorful and eye catching while still looking professional
Should not have
- pictures of cannabis buds or flowering plants.

```html
<!DOCTYPE html>
<html lang="en">
<head>
<meta charset="utf-8">
<title>Carobrook Care – Medical Marijuana Evaluations Handout</title>
<link href="https://fonts.googleapis.com/css2?family=Oswald:wght@500&family=Libre+Baskerville:wght@700&display=swap" rel="stylesheet">
<style>
  :root {
    --page-bg: #e9e6e1;
    --card-dark: #0b140f;
    --sky-blue: #63c8f2;
    --rule-blue: #8fd8f4;
    --footer-blue: #a8c2f2;
    --hours-blue: #a9cdf5;
    --number-blue: #8ec9f7;
    --white: #ffffff;
    --meadow-top: #3b4648;
    --meadow-mid: #3f5a36;
    --meadow-low: #2f4a25;
  }
  * { box-sizing: border-box; margin: 0; padding: 0; }
  html, body {
    width: 1200px; height: 1000px; overflow: hidden;
    background: var(--page-bg);
  }
  .postcard {
    position: absolute; left: 70px; top: 140px;
    width: 1060px; height: 720px;
    background: var(--card-dark);
    box-shadow: 0 6px 18px rgba(0,0,0,.35);
    overflow: hidden;
  }
  .meadow-backdrop {
    position: absolute; left: 0; top: 0; width: 1060px; height: 630px;
    background:
      radial-gradient(ellipse at 85% 85%, rgba(190,40,80,.45), transparent 45%),
      radial-gradient(ellipse at 55% 80%, rgba(110,90,190,.45), transparent 50%),
      radial-gradient(ellipse at 10% 90%, rgba(220,200,70,.35), transparent 35%),
      linear-gradient(180deg, var(--meadow-top) 0%, #4b5a4a 14%, var(--meadow-mid) 40%, var(--meadow-low) 100%);
  }
  .headline-frame {
    position: absolute; left: 105px; top: 78px;
    width: 852px; height: 158px;
    border: 2px solid var(--rule-blue);
    outline: 1px solid var(--rule-blue);
    outline-offset: -7px;
    background: rgba(20,30,30,.28);
    display: flex; flex-direction: column; justify-content: center; align-items: center;
  }
  .headline {
    font-family: "Oswald", sans-serif; font-weight: 500;
    color: var(--sky-blue);
    font-size: 45px; line-height: 54px; text-transform: uppercase;
    text-align: center; letter-spacing: .2px;
    text-shadow: 2px 3px 4px rgba(0,0,0,.7);
  }
  .hours {
    position: absolute; left: 95px; top: 310px; width: 280px;
    text-align: center;
    font-family: "Libre Baskerville", serif; font-weight: 700;
    color: var(--white);
    font-size: 22px; line-height: 32.5px;
    text-shadow: 2px 2px 3px rgba(0,0,0,.85);
  }
  .hours-title { color: var(--hours-blue); font-size: 24px; }
  .brand-seal {
    position: absolute; left: 412px; top: 300px;
    width: 230px; height: 230px; border-radius: 50%;
    background: var(--white);
    border: 5px solid #c9cfe6;
    display: flex; align-items: center; justify-content: center;
    text-align: center;
  }
  .brand-name {
    font-family: "Libre Baskerville", serif; font-weight: 700;
    color: #2f63a8; font-size: 30px; line-height: 36px;
  }
  .qualify-note {
    position: absolute; left: 655px; top: 310px; width: 340px;
    text-align: center;
    font-family: "Libre Baskerville", serif; font-weight: 700;
    color: var(--white);
    font-size: 19.5px; line-height: 30px;
    text-shadow: 2px 2px 3px rgba(0,0,0,.85);
  }
  .qualify-note .count { color: var(--number-blue); font-size: 27px; }
  .footer-band {
    position: absolute; left: 0; top: 630px; width: 1060px; height: 90px;
    border-top: 3px solid var(--rule-blue);
    background: var(--card-dark);
    display: flex; align-items: center; justify-content: center;
    font-family: "Oswald", sans-serif; font-weight: 500;
    color: var(--footer-blue); font-size: 35px; letter-spacing: .3px;
  }
  .footer-band .divider { margin: 0 18px; }
</style>
</head>
<body>
  <main class="postcard">
    <div class="meadow-backdrop" role="img" aria-label="Photograph of a wildflower meadow with purple lupines, red paintbrush and yellow blooms below misty mountains"></div>

    <div class="headline-frame">
      <h1 class="headline">Do you need a medical marijuana card?<br>We do medical marijuana evaluations!</h1>
    </div>

    <section class="hours">
      <div class="hours-title">HOURS:</div>
      <div>TUESDAY: 9 - 5</div>
      <div>WEDNESDAY: 9 - 5</div>
      <div>THURSDAY: 9 - 6</div>
      <div>FRIDAY: 9 - 7</div>
      <div>SATURDAY: 9 - 3</div>
    </section>

    <div class="brand-seal">
      <span class="brand-name">Carobrook<br>Care</span>
    </div>

    <p class="qualify-note">
      There are over <span class="count">200</span><br>
      qualifying conditions<br>
      in the state of<br>
      Massachusetts,<br>
      call today to see if<br>
      you qualify and book an<br>
      appointment!
    </p>

    <footer class="footer-band">
      <span>WWW.CAROBROOKCARE.NET</span><span class="divider">|</span><span>774-555-0138</span>
    </footer>
  </main>
</body>
</html>
```